Modern Spot UV Business Card design

We are a relatively new real estate agency. We need a business card that reflects the professionalism and prestige of our company but is also modern and fresh, based around our logo.
We would love to utilise spot UV.
Happy to let the designers use their imagination and see what they come up with (we're not very creative, so have no ideas for you, sorry) :-)
We'd like one for each staff member, but I've just provided one staff members photo here to avoid confusion.

Target Market(s)

Families

Industry/Entity Type

Real Estate Agent

Contact Information for Business Card

Colin Varga - Director & Principal
Mobile: 0491 527 806
Email: colin.varga@vbrokers.example.com.au
Phone: (08) 7364 9150
Fax: (08) 7364 9182
www.vargabrokersrealestate.example.com.au

Font styles to use
Other font styles liked:
• Kabel Dm BT

Requirements
Must have
• Contact details, logo, photo, spot UV
Nice to have
• Modern interesting features that will make people comment. Nothing too feminine nor too masculine.
Should not have
• No houses! Nothing typical of a real estate agent.

```html
<!DOCTYPE html>
<html lang="en">
<head>
<meta charset="utf-8">
<title>VargaBrokers Real Estate – Business Card</title>
<link rel="stylesheet" href="https://fonts.googleapis.com/css2?family=Open+Sans:wght@700&family=PT+Sans+Narrow:wght@400;700&family=Fira+Sans+Condensed:wght@300;400&display=swap">
<style>
  :root {
    --page-bg: #d9d9d9;
    --white: #ffffff;
    --band: #ff1a6e;
    --front-light: #f7806f;
    --front-mid: #ea3557;
    --front-dark: #a8123c;
    --back-light: #f4707a;
    --back-mid: #c4153f;
    --back-dark: #8c0b38;
    --photo-tone: #8a8d94;
  }
  * { margin: 0; padding: 0; box-sizing: border-box; }
  html, body { width: 1200px; height: 1199px; overflow: hidden; }
  body { background: var(--page-bg); position: relative; color: var(--white); font-family: "Fira Sans Condensed", sans-serif; }

  .card { position: absolute; overflow: hidden; box-shadow: 0 18px 24px rgba(0,0,0,.25); }
  .card-front { left: 143px; top: 47px; width: 875px; height: 489px; }
  .card-back { left: 150px; top: 622px; width: 871px; height: 488px; }

  .card-texture { position: absolute; inset: 0; width: 100%; height: 100%; }

  .brand-circle { position: absolute; left: 370px; top: 106px; width: 124px; height: 124px; border: 4px solid var(--white); border-radius: 50%; }
  .brand-name { position: absolute; left: 0; width: 870px; top: 238px; text-align: center; font-family: "Open Sans", sans-serif; font-weight: 700; font-size: 45px; letter-spacing: .5px; }
  .brand-sub { position: absolute; left: 274px; top: 296px; display: flex; align-items: center; }
  .brand-realestate { font-family: "PT Sans Narrow", sans-serif; font-size: 54px; line-height: 1; letter-spacing: -1px; }
  .brand-divider { width: 2px; height: 58px; background: var(--white); margin: 0 11px 0 8px; }
  .brand-tagline { font-family: "PT Sans Narrow", sans-serif; font-size: 25px; line-height: 35px; }

  .web-band { position: absolute; left: 0; top: 413px; width: 100%; height: 47px; background: var(--band); display: flex; align-items: center; justify-content: center; gap: 14px; }
  .web-band .url { font-family: "Fira Sans Condensed", sans-serif; font-size: 24px; letter-spacing: .5px; }
  .dots { display: flex; align-items: center; gap: 22px; }
  .dot { background: var(--white); border-radius: 50%; }

  .photo { position: absolute; left: 125px; top: 123px; width: 88px; height: 106px; background: linear-gradient(180deg, #c9ccd1, var(--photo-tone)); }
  .person-name { position: absolute; left: 55px; top: 244px; font-family: "PT Sans Narrow", sans-serif; font-weight: 700; font-size: 60px; line-height: 1; }
  .person-role { position: absolute; left: 85px; top: 306px; font-family: "PT Sans Narrow", sans-serif; font-size: 27px; }

  .contact { position: absolute; right: 134px; text-align: right; font-size: 23px; letter-spacing: .6px; line-height: 27px; }
  .contact-email { top: 47px; }
  .contact-phone { top: 115px; right: 147px; }
  .contact-web { top: 218px; }
  .contact-fax { top: 296px; right: 126px; }

  .icon-box { position: absolute; left: 753px; width: 51px; height: 51px; border: 2px solid var(--white); display: flex; align-items: center; justify-content: center; }
  .icon-box svg { width: 36px; height: 36px; }
</style>
</head>
<body>

<section class="card card-front" aria-label="Business card front">
  <svg class="card-texture" role="img" aria-label="Low-poly geometric facet pattern in coral, pink and crimson" viewBox="0 0 875 489" preserveAspectRatio="none">
    <defs>
      <linearGradient id="frontTone" x1="0" y1="0" x2="0.4" y2="1">
        <stop offset="0" stop-color="var(--front-light)"/>
        <stop offset=".55" stop-color="var(--front-mid)"/>
        <stop offset="1" stop-color="var(--front-dark)"/>
      </linearGradient>
    </defs>
    <rect width="875" height="489" fill="url(#frontTone)"/>
  </svg>

  <div class="brand-circle" aria-hidden="true"></div>
  <div class="brand-name">VargaBrokers</div>
  <div class="brand-sub">
    <span class="brand-realestate">Real Estate</span>
    <span class="brand-divider"></span>
    <span class="brand-tagline">Helping You Make<br>Your next move</span>
  </div>

  <div class="web-band">
    <div class="dots">
      <span class="dot" style="width:5px;height:5px"></span>
      <span class="dot" style="width:7px;height:7px"></span>
      <span class="dot" style="width:10px;height:10px"></span>
      <span class="dot" style="width:12px;height:12px"></span>
    </div>
    <span class="url">www.vargabrokersrealestate.example.com.au</span>
    <div class="dots">
      <span class="dot" style="width:12px;height:12px"></span>
      <span class="dot" style="width:10px;height:10px"></span>
      <span class="dot" style="width:7px;height:7px"></span>
      <span class="dot" style="width:5px;height:5px"></span>
    </div>
  </div>
</section>

<section class="card card-back" aria-label="Business card back">
  <svg class="card-texture" role="img" aria-label="Low-poly geometric facet pattern from coral to deep magenta" viewBox="0 0 871 488" preserveAspectRatio="none">
    <defs>
      <linearGradient id="backTone" x1="0" y1="0.6" x2="1" y2="0.3">
        <stop offset="0" stop-color="var(--back-light)"/>
        <stop offset=".45" stop-color="var(--back-mid)"/>
        <stop offset="1" stop-color="var(--back-dark)"/>
      </linearGradient>
    </defs>
    <rect width="871" height="488" fill="url(#backTone)"/>
  </svg>

  <div class="photo" role="img" aria-label="Portrait photo of Colin Varga"></div>
  <div class="person-name">Colin Varga</div>
  <div class="person-role">Director &amp; Principal</div>

  <div class="contact contact-email">colin.varga@vbrokers.example.com.au</div>
  <div class="contact contact-phone">0491 527 806<br>(08) 7364 9150</div>
  <div class="contact contact-web">www.vargabrokersrealestate.example.com.au</div>
  <div class="contact contact-fax">Fax_(08) 7364 9182</div>

  <div class="icon-box" style="top:35px" aria-label="Email">
    <svg viewBox="0 0 36 36" fill="none" stroke="#fff" stroke-width="1.6"><rect x="3" y="8" width="30" height="20"/><path d="M3 8l15 12 15-12M3 28l11-10M33 28l-11-10"/></svg>
  </div>
  <div class="icon-box" style="top:121px" aria-label="Phone">
    <svg viewBox="0 0 36 36" fill="none" stroke="#fff" stroke-width="1.8"><rect x="10" y="3" width="16" height="30" rx="3"/><rect x="12.5" y="7.5" width="11" height="19"/><circle cx="18" cy="29.5" r="1"/></svg>
  </div>
  <div class="icon-box" style="top:207px" aria-label="Website">
    <svg viewBox="0 0 36 36" fill="none" stroke="#fff" stroke-width="1.6"><circle cx="18" cy="18" r="14"/><ellipse cx="18" cy="18" rx="6" ry="14"/><path d="M4 18h28M6 11h24M6 25h24M18 4v28"/></svg>
  </div>
  <div class="icon-box" style="top:282px" aria-label="Fax">
    <svg viewBox="0 0 36 36" fill="#fff"><rect x="10" y="3" width="16" height="8"/><path d="M4 12h28v14h-5v-6H9v6H4z"/><rect x="11" y="22" width="14" height="11"/></svg>
  </div>
</section>

</body>
</html>
```